RV38

We want a trendy packaging design for our mobile accessories. Initially we will be offering TPU cases to our retail customers and than we will introduce other similar accessories such as car chargers, AC chargers, data cables etc..
We would like to see designs that are unique, practical and appealing to the general audience.
Updates

Hi Everyone

There is guaranteed payment for the best designer of this packaging.

thanks

Reason: Hi All This will give you all more time to submit your designs :) regards

Target Market(s)

Telco retail store customers

Industry/Entity Type

Retail

Requirements
Must have
• Colorful , Fun , Sexy

```html
<!DOCTYPE html>
<html lang="en">
<head>
<meta charset="utf-8">
<title>RV38 Charger Packaging</title>
<link rel="stylesheet" href="https://fonts.googleapis.com/css2?family=Comfortaa:wght@400&family=Arimo:wght@400;700&family=Tinos&display=swap">
<style>
  :root {
    --stage: #8a8a8a;
    --stage-light: #b4b4b4;
    --panel: #ffffff;
    --ink: #111111;
    --ink-soft: #2a2a2a;
    --window-dark: #3c3c3c;
    --window-light: #d9d9d9;
    --art-green: #5fa326;
    --art-green-deep: #3f7f1c;
    --art-lime: #a6cf2e;
    --art-yellow: #f5dc1e;
    --art-blue: #4fb8e3;
    --art-orange: #f29a2e;
    --art-pale: #fbf4a8;
    --label-bg: #ffffff;
  }
  * { box-sizing: border-box; margin: 0; padding: 0; }
  html, body { width: 1200px; height: 825px; overflow: hidden; }
  body {
    background: linear-gradient(180deg, var(--stage-light) 0%, var(--stage) 100%);
    position: relative;
  }
  .panel {
    position: absolute;
    top: 75px;
    width: 395px;
    height: 615px;
    background: var(--panel);
    overflow: hidden;
  }
  .panel--front { left: 145px; }
  .panel--back { left: 650px; }

  /* Front */
  .brand {
    position: absolute;
    top: 46px;
    left: 0;
    width: 100%;
    display: flex;
    justify-content: center;
    align-items: center;
    gap: 16px;
  }
  .brand__dot {
    width: 62px; height: 62px;
    border-radius: 50%;
    background: var(--ink);
  }
  .brand__name {
    font-family: "Comfortaa", sans-serif;
    font-weight: 400;
    font-size: 44px;
    color: var(--ink);
  }
  .front-art {
    position: absolute;
    left: 0; top: 210px;
    width: 100%; height: 405px;
    background: linear-gradient(160deg,
      #ffffff 0%,
      var(--art-yellow) 8%,
      var(--art-orange) 14%,
      var(--art-green) 22%,
      var(--art-blue) 32%,
      var(--art-lime) 40%,
      var(--art-yellow) 48%,
      var(--art-green-deep) 56%,
      var(--art-blue) 64%,
      var(--art-green) 72%,
      var(--art-orange) 80%,
      var(--art-yellow) 88%,
      var(--art-green) 100%);
  }
  .window {
    position: absolute;
    left: 83px; top: 137px;
    width: 292px; height: 398px;
    border-radius: 12px;
    border: 3px solid #2b2b2b;
    background: linear-gradient(160deg, var(--window-light) 0%, #9a9a9a 45%, var(--window-dark) 100%);
  }
  .model-label {
    position: absolute;
    left: 253px; top: 436px;
    width: 128px; height: 44px;
    border-radius: 22px;
    background: var(--label-bg);
    display: flex; align-items: center; justify-content: center;
    font-family: "Arimo", sans-serif;
    font-size: 14px;
    color: var(--ink);
    white-space: nowrap;
  }

  /* Back */
  .back-art {
    position: absolute;
    inset: 160px 0 0 0;
    background: linear-gradient(160deg,
      #ffffff 0%,
      var(--art-pale) 18%,
      #ffffff 34%,
      var(--art-pale) 52%,
      #fffde8 68%,
      var(--art-pale) 84%,
      #ffffff 100%);
  }
  .notes {
    position: absolute;
    left: 52px; top: 222px;
    width: 262px;
    font-family: "Tinos", serif;
    font-size: 6.6px;
    line-height: 1.75;
    color: var(--ink-soft);
    text-align: justify;
  }
  .notes p { text-indent: 18px; margin-bottom: 9px; }
  .marks {
    position: absolute;
    left: 58px; top: 452px;
    display: flex; align-items: center; gap: 28px;
  }
  .mark { background: var(--ink); }
  .mark--round { width: 38px; height: 26px; border-radius: 13px; }
  .mark--wide { width: 64px; height: 20px; border-radius: 3px; }
  .mark--circle { width: 32px; height: 32px; border-radius: 50%; background: #555; }
  .mark--square { width: 28px; height: 34px; border-radius: 2px; }
  .legal {
    position: absolute;
    left: 0; top: 524px;
    width: 100%;
    text-align: center;
    font-family: "Arimo", sans-serif;
    font-size: 10px;
    line-height: 1.25;
    color: var(--ink);
  }
</style>
</head>
<body>
  <section class="panel panel--front">
    <div class="front-art" role="img" aria-label="Colourful swirling floral illustration in green, yellow, blue and orange"></div>
    <div class="brand">
      <span class="brand__dot"></span>
      <span class="brand__name">RV38</span>
    </div>
    <div class="window" role="img" aria-label="Product window showing the black wall charger with coiled cable"></div>
    <div class="model-label">Your Model No.111</div>
  </section>

  <section class="panel panel--back">
    <div class="back-art" role="img" aria-label="Faint pale yellow floral illustration"></div>
    <div class="notes">
      <p>Thank you for choosing this charger. Before first use, read these notes with care and keep them for later reference. Plug the adapter into a standard wall outlet and connect the cable to your phone. The indicator on your device will show that charging has started. Charging time depends on the battery size and the current charge level. Do not cover the adapter while it is in use, and keep it away from water, heat and direct sunlight. Unplug it from the outlet when charging is complete or when you leave home for a long time.</p>
      <p>Use only cables that fit your device and are in good condition. Do not open or repair the adapter yourself; there are no user serviceable parts inside. Keep it out of the reach of small children. If the adapter becomes hot, makes noise or shows damage, stop using it at once. Clean it only with a dry cloth after unplugging. This product works on most mains voltages around the world, so it is a handy travel companion.</p>
    </div>
    <div class="marks">
      <span class="mark mark--round"></span>
      <span class="mark mark--wide"></span>
      <span class="mark mark--circle"></span>
      <span class="mark mark--square"></span>
    </div>
    <div class="legal">
      Copyright 2014. All rights reserved<br>
      All brands and product names are trademarks of their respective holders.
    </div>
  </section>
</body>
</html>
```